Solar energy proposal for homeowners

I am providing households with solar energy proposals, and I need a high-quality brochure that is packaged cleverly to attract the homeowner's attention. Take a look at the one page solar brochure that I have included to get an idea of text and content.

Target Market(s)

Residential Homeowners

Industry/Entity Type

Solar

Requirements
Must have
• High quality document

```html
<!DOCTYPE html>
<html lang="en">
<head>
<meta charset="UTF-8">
<title>Brightfield Energy – Solar Flyer</title>
<link href="https://fonts.googleapis.com/css2?family=Archivo:wght@500;600;700&family=Space+Grotesk:wght@400;500;600&display=swap" rel="stylesheet">
<style>
  :root {
    --lime: #a9d331;
    --lime-deep: #9cc826;
    --blue: #2a8ad9;
    --teal: #2ec6c6;
    --ink: #111511;
    --white: #ffffff;
    --black: #0b0b0b;
    --web-green: #b9e34a;
    --page: #f1f1f1;
    --photo-a: #c9d6df;
    --photo-b: #41597a;
  }
  * { box-sizing: border-box; margin: 0; padding: 0; }
  html, body { width: 1200px; height: 1200px; overflow: hidden; }
  body {
    background: var(--page);
    font-family: "Space Grotesk", Arial, sans-serif;
    color: var(--ink);
    position: relative;
  }
  .flyer {
    position: absolute; left: 203px; top: 40px;
    width: 793px; height: 1120px;
    background: radial-gradient(circle at 70% 60%, var(--lime) 0%, var(--lime-deep) 100%);
    overflow: hidden;
  }
  .brand {
    position: absolute; left: 45px; top: 62px;
    display: flex; align-items: center; gap: 16px;
    color: var(--white); font-family: "Space Grotesk", Arial, sans-serif;
    font-weight: 400; font-size: 46px; letter-spacing: -0.5px;
  }
  .brand-mark { width: 40px; height: 40px; background: var(--white); }
  .headline-box {
    position: absolute; left: 0; top: 169px; width: 425px; height: 286px;
    background: linear-gradient(90deg, var(--blue), var(--teal));
    padding: 24px 0 0 45px;
  }
  .headline {
    font-family: "Archivo", Arial, sans-serif; font-weight: 600;
    font-size: 49px; line-height: 64px; color: var(--white);
    letter-spacing: 0.3px;
  }
  .photo {
    position: absolute; left: 428px; top: 131px; width: 365px; height: 363px;
    background: linear-gradient(135deg, var(--photo-b) 0%, var(--photo-a) 55%, var(--photo-b) 100%);
  }
  .why-box { position: absolute; left: 428px; top: 494px; width: 365px; height: 300px; }
  .why-box svg { position: absolute; inset: 0; }
  .why-content { position: absolute; left: 46px; top: 70px; color: var(--white); }
  .why-title { font-family: "Archivo", Arial, sans-serif; font-weight: 600; font-size: 31px; margin-bottom: 14px; }
  .why-list { list-style: none; font-size: 14px; line-height: 16px; }
  .why-list li::before { content: "• "; }
  .tagline {
    position: absolute; left: 45px; top: 582px;
    font-size: 24px; line-height: 32px; font-weight: 500;
  }
  .about { position: absolute; left: 45px; top: 685px; width: 360px; }
  .section-title { font-family: "Archivo", Arial, sans-serif; font-weight: 600; font-size: 30px; }
  .about .section-title { margin: 0 0 8px 4px; }
  .about-text { font-size: 13.5px; line-height: 18px; }
  .services-title { position: absolute; left: 45px; top: 870px; }
  .services-arrow { position: absolute; left: 325px; top: 880px; }
  .service { position: absolute; width: 250px; }
  .service-icon {
    position: absolute; left: -50px; top: -2px; width: 35px; height: 35px;
    border-radius: 9px; background: linear-gradient(135deg, var(--blue), var(--teal));
    display: flex; align-items: center; justify-content: center;
  }
  .service-name { font-size: 12.5px; font-weight: 600; margin-bottom: 14px; }
  .service-text { font-size: 13px; line-height: 17px; }
  .footer {
    position: absolute; left: 0; bottom: 0; width: 793px; height: 63px;
    display: flex; font-size: 15.5px; color: var(--white);
  }
  .footer-contact {
    width: 485px; display: flex; align-items: center; gap: 65px; padding-left: 82px;
    background: linear-gradient(90deg, var(--blue), var(--teal));
  }
  .footer-web {
    flex: 1; background: var(--black); color: var(--web-green);
    display: flex; align-items: center; padding-left: 35px;
  }
</style>
</head>
<body>
  <main class="flyer">
    <div class="brand"><span class="brand-mark"></span>Brightfield Energy</div>

    <section class="headline-box">
      <h1 class="headline">SOLAR FOR $0<br>DOWN.<br>NO LIENS.<br>NO KIDDING.</h1>
    </section>

    <div class="photo" role="img" aria-label="Aerial photo of two installers in hard hats walking between rows of rooftop solar panels"></div>

    <section class="why-box">
      <svg width="365" height="300" viewBox="0 0 365 300">
        <defs>
          <linearGradient id="whyGradient" x1="0" y1="0" x2="1" y2="0">
            <stop offset="0" stop-color="#2a8ad9"/>
            <stop offset="1" stop-color="#2ec6c6"/>
          </linearGradient>
        </defs>
        <polygon points="0,0 365,0 365,282 62,282 0,222" fill="url(#whyGradient)"/>
        <polyline points="0,230 60,290 365,290" fill="none" stroke="#ffffff" stroke-width="4"/>
      </svg>
      <div class="why-content">
        <h2 class="why-title">Why Choose Us?</h2>
        <ul class="why-list">
          <li>No financing</li>
          <li>No liens</li>
          <li>No down payment</li>
          <li>No insurance costs</li>
          <li>No long-term commitment</li>
          <li>No maintenance costs</li>
        </ul>
      </div>
    </section>

    <p class="tagline">Power Your Future with<br>Brightfield Energy</p>

    <section class="about">
      <h2 class="section-title">About Us</h2>
      <p class="about-text">At Brightfield Energy, our mission is to make solar simple and accessible for everyone. No high-pressure sales-just the information you need to make a smart choice. With our solar rental program, you can lower your monthly energy costs and pay less current electricity bill.</p>
    </section>

    <h2 class="section-title services-title">Our Best Service</h2>
    <svg class="services-arrow" width="60" height="60" viewBox="0 0 60 60">
      <path d="M2 8 C 22 6, 36 14, 44 34" fill="none" stroke="#111511" stroke-width="2.5"/>
      <polygon points="36,34 52,32 50,52" fill="#111511"/>
    </svg>

    <div class="service" style="left:95px; top:950px;">
      <span class="service-icon"><svg width="20" height="20" viewBox="0 0 20 20"><circle cx="10" cy="8" r="5" fill="none" stroke="#fff" stroke-width="1.6"/><path d="M7.5 14h5M8 17h4" stroke="#fff" stroke-width="1.6"/></svg></span>
      <p class="service-name">Affordable &amp; Transparent</p>
      <p class="service-text">Simple pricing, no hidden fees and a fixed monthly rate lower installation, maintenance, and than typical energy bills.</p>
    </div>

    <div class="service" style="left:468px; top:950px;">
      <span class="service-icon"><svg width="20" height="20" viewBox="0 0 20 20"><circle cx="10" cy="10" r="7" fill="none" stroke="#fff" stroke-width="1.6"/><path d="M6.5 10l2.5 2.5 4.5-5" fill="none" stroke="#fff" stroke-width="1.6"/></svg></span>
      <p class="service-name">Expert Installation</p>
      <p class="service-text">Certified professionals handle installation, maintenance, and repairs end to end.</p>
    </div>

    <div class="service" style="left:95px; top:1071px;">
      <span class="service-icon"><svg width="20" height="20" viewBox="0 0 20 20"><circle cx="10" cy="10" r="7" fill="none" stroke="#fff" stroke-width="1.6"/><circle cx="10" cy="10" r="3" fill="none" stroke="#fff" stroke-width="1.6"/></svg></span>
      <p class="service-name">Local Expertise</p>
      <p class="service-text">Florida-based team that understands the needs of Orlando and statewide homeowners.</p>
    </div>

    <div class="service" style="left:468px; top:1071px;">
      <span class="service-icon"><svg width="20" height="20" viewBox="0 0 20 20"><path d="M4 16 C 4 8, 9 4, 16 4 C 16 11, 12 16, 4 16 Z M4 16 L 11 9" fill="none" stroke="#fff" stroke-width="1.6"/></svg></span>
      <p class="service-name">Eco-Friendly</p>
      <p class="service-text">Clean, renewable solar energy that helps reduce your carbon footprint.</p>
    </div>

    <footer class="footer">
      <div class="footer-contact">
        <span class="footer-phone">(407) 555-0142</span>
        <span class="footer-address">123 Anywhere St., Any City</span>
      </div>
      <div class="footer-web">www.brightfieldenergy.com</div>
    </footer>
  </main>
</body>
</html>
```